brightpathPRESS is publishing a new book and needs some exceptional cover and layout design!

We are publishing a narrow niche PDF eBook and need both a great cover AND great magazine style layout.

The eBook is a compilation of interviews with 12 financial experts on a particular topic. So the format is is the same for each interview 'chapter'

We are looking for a good front cover/document design that will make what is a pretty dry topic, exciting, interesting and easy to read. Basically - magazine style layout.

The specs for the front cover are:

Title:

The Hurdles and Openings Before Bookkeepers and Planners In Expanding Their Pension Practice In 2014 -2015

by Tom Pelliwick

published by brightpathPRESS

The client would like a similar cover to the one I have attached for your reference. (book front cover example). By no means be limited by this design suggestion. The only caveat is that shots of all interview subjects are included (except the author). These have been included in the zip file.

The design for the text should be elegant and consistent with the design of the front cover. Please format the text in pages 1 to 15 to demonstrate you've understood the brief.

Attached files.

1) MS word version of draft book pages 1 to 15
2) copy of the cover my client would like to emulate.

reminder - this is destined to be a PDF eBook - so looking for some nice eye catching magazine style layout in the design. Columns would be fine.

Good luck!

Brent Malloy
brightpathPRESS

Target Market(s)

Professional Accountants who are running there own businesses

Industry/Entity Type

Financial

Colors

Designer to choose colors to be used in the design.

Requirements
Must have
• The cover must feature headshots of all the interview subjects. The PDF layout must be optimised for viewing on an iPad

```html
<!DOCTYPE html>
<html lang="en">
<head>
<meta charset="utf-8">
<title>The Hurdles and Openings – Tom Pelliwick</title>
<link rel="stylesheet" href="https://fonts.googleapis.com/css2?family=Open+Sans:wght@400;600;700&display=swap">
<style>
  :root {
    --ink: #111111;
    --red: #ee4626;
    --blue: #1470bb;
    --green: #3aa84a;
    --lime: #8cc63f;
    --paper: #ffffff;
  }
  html, body { margin: 0; padding: 0; overflow: hidden; background: var(--paper); }
  .cover {
    position: relative;
    width: 800px; height: 1200px;
    background: var(--paper);
    font-family: "Open Sans", Arial, sans-serif;
    overflow: hidden;
  }
  .title-word { position: absolute; margin: 0; line-height: 1; white-space: nowrap; }
  .title-small { font-weight: 700; color: var(--ink); font-size: 88px; letter-spacing: -1px; }
  .title-the { left: 155px; top: 22px; }
  .title-and { left: 222px; top: 262px; }
  .title-big { font-weight: 600; font-size: 140px; letter-spacing: -2px; left: 0; right: 0; text-align: center; }
  .title-hurdles { color: var(--red); top: 112px; }
  .title-openings { color: var(--blue); top: 328px; }
  .subtitle {
    position: absolute; left: 0; right: 0; top: 484px;
    margin: 0; text-align: center;
    color: var(--green); font-weight: 400; font-size: 32px; line-height: 40px;
  }
  .panel {
    position: absolute; left: 8px; top: 644px;
    width: 784px; height: 320px;
    display: grid; grid-template-columns: repeat(8, 1fr); grid-template-rows: repeat(2, 1fr);
  }
  .headshot { background: linear-gradient(180deg, #c9ced4 0%, #8f959c 100%); }
  .headshot:nth-child(2n) { background: linear-gradient(180deg, #b7bcc2 0%, #6f757c 100%); }
  .headshot:nth-child(3n) { background: linear-gradient(180deg, #d8d2cb 0%, #9a8f86 100%); }
  .author {
    position: absolute; left: 0; right: 0; top: 1018px;
    margin: 0; text-align: center;
    color: var(--lime); font-weight: 400; font-size: 104px; line-height: 1; letter-spacing: -1px;
  }
</style>
</head>
<body>
<main class="cover">
  <h1>
    <span class="title-word title-small title-the">The</span>
    <span class="title-word title-big title-hurdles">Hurdles</span>
    <span class="title-word title-small title-and">and</span>
    <span class="title-word title-big title-openings">Openings</span>
  </h1>
  <p class="subtitle">Before Bookkeepers and Planners<br>In Expanding Their Pension Practice In<br>2014 -2015</p>
  <section class="panel" aria-label="Interview subjects">
    <div class="headshot" role="img" aria-label="Headshot of interview subject 1"></div>
    <div class="headshot" role="img" aria-label="Headshot of interview subject 2"></div>
    <div class="headshot" role="img" aria-label="Headshot of interview subject 3"></div>
    <div class="headshot" role="img" aria-label="Headshot of interview subject 4"></div>
    <div class="headshot" role="img" aria-label="Headshot of interview subject 5"></div>
    <div class="headshot" role="img" aria-label="Headshot of interview subject 6"></div>
    <div class="headshot" role="img" aria-label="Headshot of interview subject 7"></div>
    <div class="headshot" role="img" aria-label="Headshot of interview subject 8"></div>
    <div class="headshot" role="img" aria-label="Headshot of interview subject 9"></div>
    <div class="headshot" role="img" aria-label="Headshot of interview subject 10"></div>
    <div class="headshot" role="img" aria-label="Headshot of interview subject 11"></div>
    <div class="headshot" role="img" aria-label="Headshot of interview subject 12"></div>
    <div class="headshot" role="img" aria-label="Headshot of interview subject 13"></div>
    <div class="headshot" role="img" aria-label="Headshot of interview subject 14"></div>
    <div class="headshot" role="img" aria-label="Headshot of interview subject 15"></div>
    <div class="headshot" role="img" aria-label="Headshot of interview subject 16"></div>
  </section>
  <p class="author">Tom Pelliwick</p>
</main>
</body>
</html>
```